Stationary for Hair Cosmetic company

We mainly sell hair thickening products www.morvello-wellform.de/morvello-hair/ Hair thickening products are a smart and easy solution for thinning hair for both men and women. We sell very information oriented in an honest undramatic manner.

We would like to see a decent color and style that is suitable for men and women. It shall be rather modern with a vintage spin as our own product (Morvello Bottle). Please use our logo (attatched).

Please bias your design to the bottle. To give you an idea: Chalk design like http://de.pixaverum.com/id/48213597 or one-color watercolor like http://de.pixaverum.com/id/63925180 is appreciated but not necessary.

Good but rejected designs will get compensation.

Target Market(s)

Wide range in demographics: age 20-55; 45% male, 55% women; issues with hair loss; self-conscious

Industry/Entity Type

Hair

Colors
3377b5
33a6d7
32b7a4
cbdf83
fbf289
fee18a
f9bb93
f05157

Requirements
Must have
• trustworthiness
Nice to have
• Chalk design like http://de.pixaverum.com/id/48213597 or one-color watercolor like http://de.pixaverum.com/id/63925180 is appreciated but not necessary

```html
<!DOCTYPE html>
<html lang="de">
<head>
<meta charset="utf-8">
<title>Morvello Hair – Briefumschläge</title>
<link rel="stylesheet" href="https://fonts.googleapis.com/css2?family=Cinzel:wght@400;500&family=Libre+Baskerville&display=swap">
<style>
  :root {
    --backdrop: #d4e4eb;
    --paper: #fbfbfb;
    --paper-edge: #e6e9eb;
    --flap-blue: #4aaed9;
    --flap-ink: #2f6f9a;
    --ink: #2a2a2a;
    --ink-soft: #4a4a4a;
    --shadow: rgba(40, 70, 90, 0.22);
  }
  * { box-sizing: border-box; margin: 0; padding: 0; }
  html, body { width: 1200px; height: 1000px; overflow: hidden; }
  body {
    background: var(--backdrop);
    position: relative;
    font-family: "Libre Baskerville", Georgia, serif;
  }

  .envelope {
    position: absolute;
    width: 560px;
    height: 280px;
    background: var(--paper);
    border: 1px solid var(--paper-edge);
    box-shadow: 0 6px 14px var(--shadow);
    overflow: hidden;
  }

  /* Back side with the closed blue flap */
  .envelope--back { left: 130px; top: 150px; }
  .envelope__flap {
    position: absolute;
    left: 0; top: 0;
    width: 100%;
    height: 100px;
    background: var(--flap-blue);
    border-bottom-left-radius: 10px;
    border-bottom-right-radius: 10px;
    box-shadow: 0 3px 6px rgba(30, 60, 80, 0.18);
    display: flex;
    flex-direction: column;
    align-items: center;
    justify-content: center;
    gap: 6px;
  }
  .flap-mark {
    width: 30px; height: 30px;
    border-radius: 50%;
    border: 1.5px solid var(--flap-ink);
  }
  .flap-name {
    font-family: "Cinzel", "Times New Roman", serif;
    font-weight: 400;
    font-size: 11px;
    letter-spacing: 1.5px;
    color: var(--flap-ink);
  }
  .flap-rule {
    width: 150px;
    height: 1px;
    background: var(--flap-ink);
    opacity: 0.7;
  }

  /* Front side with sender block */
  .envelope--front { left: 510px; top: 570px; }
  .sender {
    position: absolute;
    left: 40px;
    bottom: 34px;
    width: 170px;
    display: flex;
    flex-direction: column;
    align-items: center;
  }
  .sender__mark {
    width: 58px; height: 66px;
    border-radius: 50%;
    border: 2px solid var(--ink);
    margin-bottom: 8px;
  }
  .sender__name {
    font-family: "Cinzel", "Times New Roman", serif;
    font-weight: 400;
    font-size: 15px;
    letter-spacing: 1.5px;
    color: var(--ink);
  }
  .sender__rule {
    width: 150px;
    height: 1px;
    background: var(--ink);
    margin: 6px 0 7px;
  }
  .sender__address {
    font-style: normal;
    font-size: 6.5px;
    line-height: 1.45;
    color: var(--ink-soft);
    text-align: center;
  }
</style>
</head>
<body>

  <section class="envelope envelope--back" aria-label="Umschlag Rückseite">
    <div class="envelope__flap">
      <span class="flap-mark" aria-hidden="true"></span>
      <span class="flap-name">Morvello Hair</span>
      <span class="flap-rule" aria-hidden="true"></span>
    </div>
  </section>

  <section class="envelope envelope--front" aria-label="Umschlag Vorderseite">
    <div class="sender">
      <span class="sender__mark" aria-hidden="true"></span>
      <span class="sender__name">Morvello Hair</span>
      <span class="sender__rule" aria-hidden="true"></span>
      <address class="sender__address">
        Halden und Rasmussen GbR<br>
        Lindauer Weg 14<br>
        61200 Brunnfeld<br>
        Tel. +49 61 55 240 318<br>
        E-Mail: kontakt@morvello-wellform.de<br>
        Web: www.morvello-wellform.de
      </address>
    </div>
  </section>

</body>
</html>
```